Business Card Design For Financial Company

Create a new design for company's business card. The corporate logo is attached in several formats. Our new website design is also attached and we would like the business cards to reflect this.
Card needs to contain the following info:
Name
Job Title
Legal company name - eg Volmar Capital (Asia) Ltd
Address - eg 612-15 Dorrance Plaza,47 Faverly Street, Hong Kong
Direct tel
Main tel
Fax
Email
Website URL
MS word format preferred. Other formats that can be edited on standard PC also OK.
Please note the the "VOLMAR" logo nameĀ font is "Gill Sans MT" on Windows
Target Market(s)
Instituation Investors
Industry/Entity Type
Business

```html
<!DOCTYPE html>
<html lang="en">
<head>
<meta charset="utf-8">
<title>Volmar Capital – Business Card</title>
<link rel="stylesheet" href="https://fonts.googleapis.com/css2?family=Arimo:wght@400;700&display=swap">
<style>
  :root {
    --bg: #1c1c1e;
    --red: #a81d24;
    --red-dark: #7d1218;
    --red-light: #c2272e;
    --white: #f4f4f4;
    --paper: #e9e9e9;
    --black: #111111;
    --silver: #d8d8d8;
    --text-light: #ffffff;
    --text-dark: #2a2a2a;
  }
  * { box-sizing: border-box; margin: 0; padding: 0; }
  html, body {
    width: 1200px; height: 984px; overflow: hidden;
    background: var(--bg);
    font-family: "Arimo", Arial, sans-serif;
  }
  .sheet {
    position: relative; width: 1200px; height: 984px;
    display: flex; flex-direction: column; align-items: center;
    justify-content: center; gap: 34px;
  }
  .card {
    position: relative; width: 770px; height: 440px; overflow: hidden;
    box-shadow: 0 10px 30px rgba(0,0,0,.55);
  }

  /* ---------- Contact side ---------- */
  .card--info { background: linear-gradient(180deg, var(--red-light), var(--red-dark)); }
  .info__top {
    position: absolute; left: 0; top: 0; width: 100%; height: 160px;
    background: linear-gradient(180deg, var(--white), var(--paper));
  }
  .brand {
    position: absolute; right: 62px; top: 58px;
  }
  .brand__name {
    font-size: 34px; letter-spacing: 7px; color: var(--text-dark); font-weight: 400;
  }
  .name-band {
    position: absolute; left: 0; top: 160px; width: 100%; height: 44px;
    background: linear-gradient(90deg, var(--black) 0%, #1d1d1d 45%, #8a8a8a 80%, var(--silver) 100%);
    display: flex; align-items: center; padding-left: 34px; gap: 34px;
  }
  .person__name { color: var(--text-light); font-weight: 700; font-size: 23px; }
  .person__title { color: var(--text-light); font-size: 15px; }
  .person__title::before { content: "| "; }
  .company {
    position: absolute; left: 34px; top: 232px; color: var(--text-light);
    font-size: 17px; line-height: 1.55; font-style: normal;
  }
  .company__legal { font-weight: 700; }
  .contacts {
    position: absolute; left: 400px; top: 232px; color: var(--text-light);
    font-size: 16px; line-height: 1.6;
    display: grid; grid-template-columns: 94px auto; column-gap: 8px;
  }
  .contacts dt { font-weight: 700; }
  .contacts dd::before { content: ": "; }

  /* ---------- Brand side ---------- */
  .card--front {
    background: linear-gradient(160deg, var(--red-light) 0%, var(--red) 45%, var(--red-dark) 100%);
  }
  .front__name {
    position: absolute; left: 60px; top: 160px;
    font-size: 64px; letter-spacing: 14px; color: var(--text-light); font-weight: 400;
  }
  .front__band {
    position: absolute; left: 0; top: 278px; width: 100%; height: 66px;
    background: linear-gradient(90deg, var(--black) 0%, #2b2b2b 30%, #9d9d9d 60%, var(--white) 100%);
    border-top: 2px solid var(--white);
    display: flex; align-items: center; padding-left: 60px;
  }
  .front__url { color: var(--text-light); font-size: 18px; letter-spacing: 3px; font-weight: 700; }
</style>
</head>
<body>
<main class="sheet">

  <section class="card card--info" aria-label="Business card, contact side">
    <div class="info__top">
      <div class="brand">
        <span class="brand__name">VOLMAR</span>
      </div>
    </div>
    <div class="name-band">
      <span class="person__name">Daniel Marsh</span>
      <span class="person__title">Job Title</span>
    </div>
    <address class="company">
      <div class="company__legal">Volmar Capital (Asia) Ltd</div>
      <div>612-15 Dorrance Plaza,</div>
      <div>47 Faverly Street,</div>
      <div>Hong Kong</div>
    </address>
    <dl class="contacts">
      <dt>Direct tel</dt><dd>+00 123 456 789</dd>
      <dt>Main tel</dt><dd>+00 123 456 789</dd>
      <dt>Fax</dt><dd>+00 123 456 789</dd>
      <dt>Email</dt><dd>office@volmarcapital.com</dd>
    </dl>
  </section>

  <section class="card card--front" aria-label="Business card, brand side">
    <div class="front__name">VOLMAR</div>
    <div class="front__band">
      <span class="front__url">www.volmarcapital.com</span>
    </div>
  </section>

</main>
</body>
</html>
```